Venture Capital firm needs modern business cards

We are a Venture Capital firm within financial services/Asset management. The industry generally has basic business cards with black, blue and maybe green/yellow design elements.
Our firm has a four-colour swoosh logo. We are based in London and want to stand out, just a little bit!, from the crowd. Our company is called MOBRA Holdings and the 'C' stands for collaboration thus using pixelfair is a natural portal for our business card design competition. Our logo came via pixelfair too!
We use 'Venture Partner in Asset Management' as our tagline and this is Trademark registered. We operate in a conservative industry and we should not overstep our mark. The logo is colorful as it is and therefore the rest of the design should not be too fanciful.
The objective is twofold: make our logo element stick and memorable with our audience, whilst representing a conservative yet young image.
Updates
The Business Card obviously needs a field for Name, Surname, Job Title, Adress fields: Street, City, Postcode, Country, telefone and cell number, website address, etc.
We have uploaded the ai file. We trust that these are OK. If not, please advise.
Reason: We have have been busy with a client engagement. We will set the project as Guaranteed in return for the troubles we cause. Apologies for the confusion.
Thank you all for these great and creative design suggestions. The team is very happy with a number of your ideas! We will be in touch tomorrow to give individual feedback before the project closes on Friday. We look forward to working with some of you to narrow down your creations. Thank you, MOBRA Holdings team.
All,
Target Market(s)
Financial Services Professionals, Investors, Media, 35-70 years, mainly male, well educated
Industry/Entity Type
Conservative
Requirements
Must have
- We must make use of our logo and potential tagline 'Venture Partner in Asset Management' as we are establishing a new Brand and new company in the market.
We can use 'MOBRA', 'MOBRA Holdings', and 'MOBRA Holdings'+tagline 'Venture Partner in Asset Management' or simply the four-colour swoosh plus the name of the company as part of the text. (see files)
All design elements are available in black or grey-scale if required. (grey scale swoosh attached).
Due to regulation we must have the following wording on the card in small print 'MOBRA Holdings is an Appointed Representative of Warbeck Ledger Advisory Limited, which is authorised by the Monetary Standards Bureau'.
Nice to have
- We would consider designs that make use of different printing techniques such embossing/debossing, UV spot etc.
We attach our colour palette in the files section for your reference.
Should not have
- The font we use for our company name is 'EXO' so do not use a font style that clashes with the corporate fonts, please.
Do not use other design elements than the ones we provide in the file library as part of this project.

```html
<!DOCTYPE html>
<html lang="en">
<head>
<meta charset="utf-8">
<title>MOBRA Holdings – Business Card</title>
<link rel="stylesheet" href="https://fonts.googleapis.com/css2?family=Arimo:wght@400;700&display=swap">
<style>
  :root {
    --page-bg: #e6e6e8;
    --card-grey: #d3d3d5;
    --card-edge: #ffffff;
    --band-white: #ffffff;
    --ink: #3d3d3f;
    --ink-soft: #5a5a5c;
    --ink-faint: #7a7a7c;
    --mark: #9a9a9c;
  }
  html, body {
    margin: 0;
    padding: 0;
    width: 1200px;
    height: 520px;
    overflow: hidden;
    background: var(--page-bg);
    font-family: "Arimo", Arial, sans-serif;
  }
  .sheet {
    width: 1200px;
    height: 520px;
    display: flex;
    align-items: center;
    justify-content: center;
    gap: 48px;
  }
  .card {
    position: relative;
    width: 527px;
    height: 300px;
    box-sizing: border-box;
    border: 6px solid var(--card-edge);
    border-radius: 16px;
    background: var(--card-grey);
    box-shadow: 0 14px 18px -10px rgba(0,0,0,0.35);
    overflow: hidden;
  }

  /* Front */
  .front-band {
    position: absolute;
    left: 0; right: 0;
    top: 172px;
    height: 84px;
    background: var(--band-white);
    display: flex;
    align-items: center;
    justify-content: center;
  }
  .brand {
    display: flex;
    align-items: center;
    gap: 12px;
  }
  .brand-dot {
    width: 34px;
    height: 34px;
    border-radius: 50%;
    background: var(--mark);
  }
  .brand-name {
    font-size: 40px;
    font-weight: 700;
    color: var(--ink);
    line-height: 1;
    letter-spacing: 1px;
  }

  /* Back */
  .back-mark {
    position: absolute;
    left: 78px;
    top: 78px;
    width: 92px;
    height: 92px;
    border-radius: 50%;
    background: var(--mark);
  }
  .contact {
    position: absolute;
    left: 234px;
    top: 30px;
    color: var(--ink-soft);
  }
  .contact-name {
    font-size: 19px;
    margin: 0;
  }
  .contact-role {
    font-size: 14px;
    margin: 2px 0 14px;
    color: var(--ink);
  }
  .contact-list {
    list-style: none;
    margin: 0;
    padding: 0;
    font-size: 15px;
  }
  .contact-list li {
    display: flex;
    margin-bottom: 11px;
  }
  .contact-key {
    width: 26px;
    color: var(--ink);
  }
  .address {
    position: absolute;
    left: 0; right: 0;
    bottom: 38px;
    text-align: center;
    font-size: 15px;
    color: var(--ink-soft);
    margin: 0;
  }
  .legal {
    position: absolute;
    left: 0; right: 0;
    bottom: 10px;
    text-align: center;
    font-size: 10px;
    line-height: 1.2;
    color: var(--ink-faint);
    margin: 0;
  }
</style>
</head>
<body>
<main class="sheet">
  <section class="card card-front" aria-label="Card front">
    <div class="front-band">
      <div class="brand">
        <span class="brand-dot"></span>
        <span class="brand-name">MOBRA</span>
      </div>
    </div>
  </section>

  <section class="card card-back" aria-label="Card back">
    <span class="back-mark"></span>
    <div class="contact">
      <p class="contact-name">Daniel Hartley</p>
      <p class="contact-role">Chairman</p>
      <ul class="contact-list">
        <li><span class="contact-key">e</span>daniel@mobraholdings.com</li>
        <li><span class="contact-key">w</span>www.mobraholdings.com</li>
        <li><span class="contact-key">t</span>+1 (800) 555-0142</li>
        <li><span class="contact-key">m</span>+1 (800) 555-0142</li>
      </ul>
    </div>
    <p class="address">17 Carrow Street, 9 Fenmore Square, London, United Kingdom</p>
    <p class="legal">MOBRA Holdings is an Appointed Representative of Warbeck Ledger Advisory Limited,<br>which is authorised by the Monetary Standards Bureau.</p>
  </section>
</main>
</body>
</html>
```